Modern and Elegant business card

A clean and modern but traditional business card is required to reflect the updated LOGO and the new website www.brightkestrel.com

The old card as provided is a bit disjointed, crowded and not clear to read especially the company name which is almost hidden in the logo.

The card should take it's queues from the colours of the logo which are green, yellow and orange, bold but rich, not faded or washed out.

We are looking to drastically clean up and improve our old cards

Target Market(s)

Professional Consulting and Business/Government

Industry/Entity Type

Management Consulting

Contact Information for Business Card

The card needs to outlined the new Service Groups as seen on the new site: http://brightkestrel.com/services/ New logo needs to be included
The usual info for phones, address and name and email

Font styles to use
Serif
Sans Serif

Colors
fbee3d
f78f20
9bcb3c

Requirements
Must have
• New logo as seen on the current site and provided here
• Service Groups as seen http://brightkestrel.com/services/
• Needs to be functional and clean, well proportioned and organized
Nice to have
• Name of cities where offices are located

```html
<!DOCTYPE html>
<html lang="en">
<head>
<meta charset="utf-8">
<title>Bright Kestrel – Business Card</title>
<link rel="stylesheet" href="https://fonts.googleapis.com/css2?family=Cinzel:wght@500&family=Source+Sans+3:wght@400;500&display=swap">
<style>
  :root {
    --stage: #bcbdbf;
    --paper: #ffffff;
    --ink: #000000;
    --text-dark: #1a1a1a;
    --text-light: #ffffff;
    --red: #e8412c;
    --orange: #f78f20;
    --yellow: #fbee3d;
    --divider: #333333;
  }
  * { box-sizing: border-box; margin: 0; padding: 0; }
  html, body { width: 1200px; height: 1000px; overflow: hidden; }
  body {
    background: var(--stage);
    font-family: "Source Sans 3", Arial, sans-serif;
    position: relative;
  }
  .card {
    position: absolute;
    left: 250px;
    width: 701px;
    height: 411px;
    overflow: hidden;
  }
  .card--front { top: 61px; background: var(--paper); }
  .card--back { top: 529px; background: var(--ink); color: var(--text-light); }

  .brand {
    position: absolute;
    font-family: "Cinzel", Georgia, serif;
    font-weight: 500;
    line-height: 1.02;
    letter-spacing: 1px;
    text-align: center;
  }
  .brand__mark {
    display: block;
    width: 46px; height: 46px;
    border-radius: 50%;
    background: var(--orange);
    margin: 0 auto 16px;
  }
  .card--front .brand { left: 40px; top: 36px; width: 210px; font-size: 34px; color: var(--ink); }
  .card--back .brand { left: 36px; top: 36px; width: 222px; font-size: 36px; color: var(--text-light); }

  .speed-lines { position: absolute; left: 304px; top: 120px; }

  .rule-gradient {
    position: absolute; left: 0; width: 100%; height: 3px;
    background: linear-gradient(90deg, var(--red), var(--orange) 40%, var(--yellow) 70%, var(--red));
  }
  .card--front .rule-gradient { top: 193px; }
  .card--back .rule-gradient { top: 222px; }

  .name-band {
    position: absolute; left: 0; top: 196px; width: 100%; height: 77px;
    background: var(--ink); color: var(--text-light);
    padding: 12px 0 0 42px;
  }
  .name-band__name { font-family: "Cinzel", Georgia, serif; font-weight: 500; font-size: 33px; line-height: 1; }
  .name-band__title { font-size: 21px; line-height: 1.2; margin-top: 2px; }

  .contacts {
    position: absolute; top: 318px; left: 35px;
    display: flex; font-size: 15.5px; line-height: 18px; color: var(--text-dark);
  }
  .contacts__col { padding-right: 12px; }
  .contacts__col + .contacts__col { border-left: 1px solid var(--divider); padding-left: 13px; }
  .contacts__col--usa { width: 195px; }
  .contacts__col--canada { width: 210px; padding-right: 0; }
  .contacts__col--address { padding-left: 17px; }
  .contacts__heading { font-size: 17px; font-weight: 500; line-height: 20px; }

  .services {
    position: absolute; left: 278px; top: 41px; list-style: none;
    font-size: 14.5px; line-height: 23.8px;
  }
  .services li { display: flex; align-items: center; white-space: nowrap; }
  .services svg { margin-right: 9px; flex: none; }

  .flag {
    position: absolute; left: 50px;
    width: 56px; height: 56px; border-radius: 50%;
    border: 2px solid #d9d9d9;
  }
  .flag--ca { top: 252px; background: radial-gradient(circle, #ffffff 35%, #d52b1e 37%); }
  .flag--us { top: 324px; background: linear-gradient(180deg, #3c3b6e 0 45%, #b22234 45% 60%, #ffffff 60% 70%, #b22234 70%); }

  .city { position: absolute; font-size: 16.5px; line-height: 17px; white-space: nowrap; }
  .city small { display: block; font-size: 13.5px; line-height: 16px; }
  .city--ca { top: 264px; }
  .city--us { top: 336px; }
  .city--edmonton { left: 131px; }
  .city--calgary { left: 235px; }
  .city--vancouver { left: 326px; }
  .city--toronto { left: 459px; }
  .city--ottawa { left: 555px; }
  .city--detroit { left: 128px; }
  .city--washington { left: 210px; }
  .city--seattle { left: 321px; }
  .city--houston { left: 414px; }
  .city--palm-beach { left: 510px; }
</style>
</head>
<body>
  <section class="card card--front">
    <div class="brand"><span class="brand__mark"></span>BRIGHT<br>KESTREL</div>
    <svg class="speed-lines" width="397" height="35" viewBox="0 0 397 35" aria-hidden="true">
      <defs>
        <linearGradient id="line-fade" x1="0" x2="1">
          <stop offset="0" stop-color="#e8412c"/>
          <stop offset="0.6" stop-color="#f78f20"/>
          <stop offset="1" stop-color="#fbee3d"/>
        </linearGradient>
      </defs>
      <rect x="66" y="1" width="331" height="2" fill="url(#line-fade)"/>
      <rect x="0" y="10" width="397" height="2" fill="url(#line-fade)"/>
      <rect x="41" y="20" width="356" height="2" fill="url(#line-fade)"/>
      <rect x="134" y="29" width="263" height="2" fill="url(#line-fade)"/>
    </svg>
    <div class="rule-gradient"></div>
    <div class="name-band">
      <div class="name-band__name">YOUR NAME</div>
      <div class="name-band__title">Title</div>
    </div>
    <div class="contacts">
      <div class="contacts__col contacts__col--usa">
        <div class="contacts__heading">USA</div>
        Direct: +1 555 302 0147<br>info@brightkestrel.com
      </div>
      <div class="contacts__col contacts__col--canada">
        <div class="contacts__heading">CANADA</div>
        Direct: +1 555 758 0192<br>info@brightkestrel.com
      </div>
      <div class="contacts__col contacts__col--address">
        1200 - 45B Avenue NW,<br>Edmonton AB Canada T0X 1A1<br>www.brightkestrel.com
      </div>
    </div>
  </section>

  <section class="card card--back">
    <div class="brand"><span class="brand__mark"></span>BRIGHT<br>KESTREL</div>
    <ul class="services">
      <li><svg width="15" height="17" viewBox="0 0 15 17"><path d="M1 8 L6 16 L14 1 L6 10 Z" fill="#f78f20"/></svg>Export Market Development</li>
      <li><svg width="15" height="17" viewBox="0 0 15 17"><path d="M1 8 L6 16 L14 1 L6 10 Z" fill="#f78f20"/></svg>Community and Economic Development</li>
      <li><svg width="15" height="17" viewBox="0 0 15 17"><path d="M1 8 L6 16 L14 1 L6 10 Z" fill="#f78f20"/></svg>Business Strategy, Implementation and Project Management</li>
      <li><svg width="15" height="17" viewBox="0 0 15 17"><path d="M1 8 L6 16 L14 1 L6 10 Z" fill="#f78f20"/></svg>Commercial/Retail Business Optimization Strategy</li>
      <li><svg width="15" height="17" viewBox="0 0 15 17"><path d="M1 8 L6 16 L14 1 L6 10 Z" fill="#f78f20"/></svg>Energy Sector Strategy and Supply Chain Optimization</li>
      <li><svg width="15" height="17" viewBox="0 0 15 17"><path d="M1 8 L6 16 L14 1 L6 10 Z" fill="#f78f20"/></svg>Strategic Communications, Branding and Social Media</li>
    </ul>
    <div class="rule-gradient"></div>

    <div class="flag flag--ca" role="img" aria-label="Round Canadian flag badge"></div>
    <div class="city city--ca city--edmonton">Edmonton<small>Alperta</small></div>
    <div class="city city--ca city--calgary">Calgary<small>Alperta</small></div>
    <div class="city city--ca city--vancouver">Vancouver<small>British Columpia</small></div>
    <div class="city city--ca city--toronto">Toronto<small>Ontario</small></div>
    <div class="city city--ca city--ottawa">Ottawa<small>Ontario</small></div>

    <div class="flag flag--us" role="img" aria-label="Round United States flag badge"></div>
    <div class="city city--us city--detroit">Detroit<small>Michigan</small></div>
    <div class="city city--us city--washington">Washington<small>D.C.</small></div>
    <div class="city city--us city--seattle">Seattle<small>Washington</small></div>
    <div class="city city--us city--houston">Houston<small>Texas</small></div>
    <div class="city city--us city--palm-beach">West Palm Beach<small>Florida</small></div>
  </section>
</body>
</html>
```